****Amazing Solar Energy Company | Needs A Dynamic Website In Wordpress ****

Here at Brivane Solar, our approach is straightforward: we listen, educate, and collaborate. We are a Residential & Commercial solar energy company located in Sanford, FL. OLD TEMP Website https://www.brivanesolar-example.com/

We are looking for a dynamic website design, layout, and code in Wordpress. We will be using a builder (Elementor) post-install so keep that in mind.

IMPORTANT:
Please See brand kit, font type, site map, and even a rough home page. We even have persona targets if needed.

Please review all images and documents uploaded as well

Please rely on your own design with the goal to educate the consumer on the many benefits of solar energy.

Target Market(s)

Home Owners who are looking for Solar Panels

Industry/Entity Type

Solar Energy, Solar Panels, Green Energy

Coding

Coded - Design and coding required

Number of Pages Required

5+ page

Font styles to use
Other font styles liked:
• Header: Raleway Body Text: Montserrat

Colors

Designer to choose colors to be used in the design.

Requirements
Must have
• Must follow the brand kit color, fonts etc | Must be clean and engaging | Modern, Simplistic, Impact, Clean, Cooling, Calming
Nice to have
• Rotating Header, Step By Steps Visuals

```html
<!DOCTYPE html>
<html lang="en">
<head>
<meta charset="utf-8">
<title>Brivane Solar – Building Bright Partnerships</title>
<link rel="stylesheet" href="https://fonts.googleapis.com/css2?family=Montserrat:wght@400;500;600;700&family=Raleway:wght@700;800&display=swap">
<style>
:root{
  --teal:#2a9d8a;
  --navy:#243b4a;
  --navy-deep:#1d303d;
  --orange:#e8674a;
  --yellow:#efbf5a;
  --peach:#f4a25d;
  --ink:#2b3a44;
  --muted:#6b7780;
  --grey-bg:#f1f1f1;
  --white:#ffffff;
}
*{box-sizing:border-box;margin:0;padding:0}
html,body{width:1200px;height:4584px;overflow:hidden}
body{position:relative;background:var(--white);font-family:"Montserrat",sans-serif;color:var(--ink)}
.abs{position:absolute}
h1,h2,h3,.display{font-family:"Raleway",sans-serif}
.btn-outline{position:absolute;display:flex;align-items:center;justify-content:center;border:2px solid var(--orange);color:var(--navy);font-weight:700;font-size:12px;letter-spacing:.5px;background:var(--white)}

/* header */
.topbar{position:absolute;left:650px;top:0;width:550px;height:34px;background:var(--teal);clip-path:polygon(22px 0,100% 0,100% 100%,0 100%)}
.social-top{position:absolute;top:10px;width:14px;height:14px;border-radius:3px;background:var(--white)}
.login{position:absolute;left:1050px;top:10px;color:var(--white);font-size:11px;font-weight:700;display:flex;gap:6px;align-items:center}
.brand{position:absolute;display:flex;align-items:center;gap:10px;font-family:"Raleway",sans-serif;font-weight:800;letter-spacing:2px;text-transform:uppercase;white-space:nowrap}
.brand-dot{border-radius:50%;background:var(--yellow)}
.nav{position:absolute;left:388px;top:72px;display:flex;gap:17px;font-size:11px;font-weight:600;color:var(--navy)}
.nav .active{color:var(--orange)}
.callus{position:absolute;left:948px;top:62px;display:flex;align-items:center;gap:10px}
.callus .ring{width:36px;height:36px;border-radius:50%;background:var(--orange);display:flex;align-items:center;justify-content:center}
.callus small{display:block;font-size:10px;color:var(--muted);font-weight:500}
.callus strong{font-size:17px;color:var(--navy);font-weight:700}

/* hero */
.hero-photo{position:absolute;left:0;top:125px;width:1200px;height:800px;background:linear-gradient(160deg,#3f7fb6 0%,#6b9cc0 28%,#8a5a45 52%,#a0503a 70%,#6d3a2c 100%)}
.hero-shape{position:absolute;left:0;top:0;width:1200px;height:960px}
.hero-kicker{position:absolute;left:90px;top:262px;color:var(--white);font-size:12px;font-weight:600;letter-spacing:.5px}
.hero-title{position:absolute;left:88px;top:290px;color:var(--white);font-size:62px;font-weight:800;line-height:1.15}
.hero-btn{position:absolute;left:89px;top:458px;width:148px;height:42px;background:var(--orange);color:var(--white);font-size:12px;font-weight:700;display:flex;align-items:center;justify-content:center}
.hero-line{position:absolute;left:599px;top:835px;width:1px;height:108px;background:var(--teal)}

/* services */
.sec-title{position:absolute;left:0;width:1200px;text-align:center;color:var(--navy);font-weight:800}
.card{position:absolute;top:1086px;width:351px;height:463px;background:var(--white);box-shadow:0 10px 30px rgba(0,0,0,.12);text-align:center}
.card-photo{position:absolute;left:10px;top:10px;width:331px;height:222px}
.card h3{position:absolute;top:256px;width:100%;font-size:19px;color:var(--navy)}
.card p{position:absolute;top:290px;left:45px;width:261px;font-size:13px;line-height:21px;color:var(--muted)}

/* why choose */
.feature{position:absolute;width:235px}
.feature h4{font-size:15px;color:var(--navy);font-weight:700;margin-bottom:4px}
.feature p{font-size:11.5px;line-height:17px;color:var(--muted)}
.feature.right{text-align:right}
.icon-bub{position:absolute;width:64px;height:64px;border-radius:50%;background:var(--teal);display:flex;align-items:center;justify-content:center}

/* about */
.about-bg{position:absolute;left:0;top:2079px;width:1200px;height:770px}
.about-art{position:absolute;left:120px;top:2150px;width:500px;height:560px;background:radial-gradient(circle at 60% 45%,rgba(239,191,90,.55) 0%,rgba(232,103,74,.25) 40%,rgba(241,241,241,0) 70%)}
.about-panel{position:absolute;left:147px;top:111px;width:249px;height:418px;background:linear-gradient(180deg,#2d4a66,#1c2e42);transform:skewY(-1deg)}
.panels-photo{position:absolute;left:917px;top:2563px;width:283px;height:134px;background:linear-gradient(160deg,#3457a8,#1f3576 60%,#9aa4b5);clip-path:polygon(0 35%,100% 0,100% 55%,10% 100%)}
.about-copy{position:absolute;left:659px;top:2228px;width:420px}
.about-copy h2{font-size:34px;color:var(--navy)}
.about-copy .sub{font-size:11.5px;font-weight:600;color:var(--navy);margin-top:6px}
.about-copy p{font-size:13px;line-height:23px;color:var(--muted);margin-top:18px}

/* reasons */
.reason{position:absolute;width:250px}
.reason h4{font-size:14.5px;color:var(--navy);font-weight:700;margin-bottom:4px}
.reason p{font-size:11.5px;line-height:18px;color:var(--muted)}
.reason-bub{position:absolute;width:90px;height:90px;border-radius:50%;display:flex;align-items:center;justify-content:center;box-shadow:0 0 0 6px #fff}

/* team */
.team-photo{position:absolute;left:0;top:3560px;width:1200px;height:720px;background:linear-gradient(180deg,#ffffff 0%,#c9d7c2 14%,#7f9a6e 35%,#365a86 55%,#2d4f7e 75%,#6d8a4a 100%)}

/* footer */
.footer-shape{position:absolute;left:0;top:3960px;width:1200px;height:624px}
.foot-h{position:absolute;top:4232px;font-family:"Raleway",sans-serif;font-weight:700;color:var(--white);font-size:19px}
.contact-item{position:absolute;left:377px;display:flex;gap:10px;color:#d6dde2;font-size:12px;line-height:19px}
.contact-item b{color:var(--white);font-weight:600;display:block}
.post{position:absolute;left:616px;display:flex;gap:12px;width:210px;padding-bottom:10px;border-bottom:1px solid rgba(255,255,255,.15)}
.thumb{width:54px;height:36px;background:linear-gradient(135deg,#7fa3c4,#5c7a4c)}
.post b{display:block;color:var(--white);font-size:12px;font-weight:600}
.post span{color:#aeb9c1;font-size:10.5px}
.work{position:absolute;width:73px;height:73px;background:linear-gradient(145deg,#8fb1d3,#3f5f8a 60%,#6f8a58)}
.soc{width:34px;height:34px;border-radius:50%;background:rgba(255,255,255,.15)}
.copyright{position:absolute;left:0;top:4530px;width:1200px;height:54px;background:var(--navy-deep);color:var(--white);font-size:11.5px;font-weight:500;display:flex;align-items:center;justify-content:center}
.chat{position:absolute;left:1130px;top:4510px;width:50px;height:50px;border-radius:50%;background:var(--orange);display:flex;align-items:center;justify-content:center}
</style>
</head>
<body>

<!-- header -->
<div class="topbar"></div>
<div class="social-top" style="left:692px"></div>
<div class="social-top" style="left:741px"></div>
<div class="social-top" style="left:790px"></div>
<div class="social-top" style="left:845px"></div>
<div class="login"><svg width="10" height="11" viewBox="0 0 10 11"><circle cx="5" cy="3" r="2.6" fill="#fff"/><path d="M0 11c0-3.3 2.2-5 5-5s5 1.7 5 5z" fill="#fff"/></svg>LOGIN</div>

<div class="brand" style="left:88px;top:46px;color:var(--navy);font-size:26px"><span class="brand-dot" style="width:22px;height:22px"></span>Brivane Solar</div>

<nav class="nav">
  <span class="active">HOME</span><span>ABOUT</span><span>LEARN MORE</span><span>CAREERS</span><span>CONNECT</span><span>WEBINAR</span><span>BLOG</span><span>CONTACT</span>
</nav>
<div class="callus">
  <div class="ring"><svg width="16" height="16" viewBox="0 0 24 24"><path d="M6.6 10.8a15.1 15.1 0 006.6 6.6l2.2-2.2c.3-.3.7-.4 1-.2 1.1.4 2.3.6 3.6.6.6 0 1 .4 1 1V20c0 .6-.4 1-1 1A17 17 0 013 4c0-.6.4-1 1-1h3.5c.6 0 1 .4 1 1 0 1.3.2 2.5.6 3.6.1.3 0 .7-.2 1z" fill="#fff"/></svg></div>
  <div><small>CALL US</small><strong>555.014.2290</strong></div>
</div>

<!-- hero -->
<div class="hero-photo" role="img" aria-label="Photo of a red brick house with rooftop solar panels under a blue sky"></div>
<svg class="hero-shape" viewBox="0 0 1200 960" aria-hidden="true">
  <polygon points="356,763 872,905 1200,705 1200,725 872,935" fill="#2a9d8a"/>
  <polygon points="0,645 872,935 1200,725 1200,960 0,960" fill="#ffffff"/>
</svg>
<div class="hero-kicker">WELCOME BRIVANE SOLAR</div>
<h1 class="hero-title">Building Bright<br>Partnerships</h1>
<div class="hero-btn">LEARN MORE</div>
<div class="hero-line"></div>

<!-- services -->
<h2 class="sec-title" style="top:966px;font-size:35px;line-height:44px">Interested in Exploring Solar?<br>We’re Here to Help.</h2>

<div class="card" style="left:240px">
  <div class="card-photo" role="img" aria-label="Photo of a blue residential house with solar panels on the roof" style="background:linear-gradient(170deg,#7fb2e0 0%,#a9cdee 40%,#2f4763 65%,#4f7a3f 100%)"></div>
  <h3>Residential</h3>
  <p>Take power into your own hands by booking an educational consultation to learn more about the residential solar industry.</p>
  <div class="btn-outline" style="left:112px;top:391px;width:127px;height:38px">LEARN MORE</div>
</div>
<div class="card" style="left:609px">
  <div class="card-photo" role="img" aria-label="Photo of a commercial solar array at sunset with a city skyline" style="background:linear-gradient(180deg,#7d96b3 0%,#e9b98a 35%,#3d7fc4 55%,#2a5f9e 80%,#3b5d2f 100%)"></div>
  <h3>Commercial</h3>
  <p>Take your business to the next level by booking an educational consultation to learn more about the commercial solar industry.</p>
  <div class="btn-outline" style="left:112px;top:391px;width:127px;height:38px">LEARN MORE</div>
</div>

<!-- why choose -->
<h2 class="sec-title" style="top:1636px;font-size:34px">Why Choose Brivane Solar?</h2>
<svg class="abs" style="left:400px;top:1700px" width="400" height="330" viewBox="0 0 400 330" aria-hidden="true">
  <path d="M118 48 A150 150 0 0 1 285 48" fill="none" stroke="#243b4a" stroke-width="1.2" stroke-dasharray="4 4"/>
  <line x1="85" y1="80" x2="66" y2="120" stroke="#243b4a" stroke-width="1.2"/>
  <line x1="310" y1="80" x2="330" y2="120" stroke="#243b4a" stroke-width="1.2"/>
  <line x1="66" y1="180" x2="70" y2="218" stroke="#243b4a" stroke-width="1.2"/>
  <line x1="340" y1="180" x2="333" y2="218" stroke="#243b4a" stroke-width="1.2"/>
  <circle cx="89" cy="75" r="5" fill="#fff" stroke="#243b4a" stroke-width="1.5"/>
  <circle cx="314" cy="75" r="5" fill="#fff" stroke="#243b4a" stroke-width="1.5"/>
  <circle cx="67" cy="195" r="5" fill="#fff" stroke="#243b4a" stroke-width="1.5"/>
  <circle cx="337" cy="195" r="5" fill="#fff" stroke="#243b4a" stroke-width="1.5"/>
  <circle cx="202" cy="173" r="107" fill="#243b4a"/>
  <text x="202" y="182" text-anchor="middle" font-family="Raleway, sans-serif" font-weight="800" font-size="26" fill="#ffffff">Brivane</text>
</svg>

<div class="icon-bub" style="left:486px;top:1716px"><svg width="30" height="30" viewBox="0 0 30 30" fill="none" stroke="#fff" stroke-width="1.8"><circle cx="15" cy="9" r="4"/><circle cx="7" cy="12" r="3"/><circle cx="23" cy="12" r="3"/><path d="M8 26c0-4 3-7 7-7s7 3 7 7M2 24c0-3 2-5 5-5M28 24c0-3-2-5-5-5"/></svg></div>
<div class="icon-bub" style="left:653px;top:1716px"><svg width="30" height="30" viewBox="0 0 30 30" fill="none" stroke="#fff" stroke-width="1.8"><circle cx="15" cy="15" r="5"/><circle cx="15" cy="15" r="11" stroke-dasharray="4 3"/></svg></div>
<div class="icon-bub" style="left:425px;top:1816px"><svg width="30" height="30" viewBox="0 0 30 30" fill="none" stroke="#fff" stroke-width="1.8"><circle cx="15" cy="12" r="8"/><path d="M10 19l-3 9 8-3 8 3-3-9"/></svg></div>
<div class="icon-bub" style="left:714px;top:1816px"><svg width="30" height="30" viewBox="0 0 30 30" fill="none" stroke="#fff" stroke-width="1.8"><path d="M5 15a10 10 0 0117-7M25 15a10 10 0 01-17 7"/><path d="M22 3v5h-5M8 27v-5h5"/></svg></div>
<div class="icon-bub" style="left:438px;top:1915px"><svg width="30" height="30" viewBox="0 0 30 30" fill="none" stroke="#fff" stroke-width="1.8"><path d="M9 27v-6c-3-2-4-5-4-8a10 10 0 0120 0l2 5h-3v4h-5v5"/><circle cx="15" cy="12" r="3"/></svg></div>
<div class="icon-bub" style="left:701px;top:1915px"><svg width="30" height="30" viewBox="0 0 30 30" fill="none" stroke="#fff" stroke-width="1.8"><path d="M2 11l13-6 13 6-13 6z"/><path d="M7 14v7c4 3 12 3 16 0v-7"/></svg></div>

<div class="feature right" style="left:233px;top:1714px"><h4>Teamwork</h4><p>Your partner from the initial consult throughout the life of your system.</p></div>
<div class="feature" style="left:737px;top:1714px"><h4>Integration</h4><p>Manage your system with our exclusive apps and online tools.</p></div>
<div class="feature right" style="left:170px;top:1817px;width:235px"><h4>Quality</h4><p>Collaborating with the best in the solar industry.</p></div>
<div class="feature" style="left:796px;top:1817px;width:215px"><h4>Efficiency</h4><p>The entire process is streamlined, making it simple for you.</p></div>
<div class="feature right" style="left:185px;top:1923px;width:235px"><h4>Expertise</h4><p>Our contractors are held to the highest of standards.</p></div>
<div class="feature" style="left:783px;top:1923px;width:230px"><h4>Education</h4><p>Free training and educational tools available.</p></div>

<!-- about -->
<svg class="about-bg" viewBox="0 2079 1200 770" aria-hidden="true">
  <rect x="0" y="2079" width="1200" height="770" fill="#f1f1f1"/>
  <polygon points="0,2575 340,2830 1200,2620 1200,2640 340,2848 0,2595" fill="#dcdfe1"/>
  <polygon points="0,2595 340,2848 1200,2640 1200,2849 0,2849" fill="#ffffff"/>
</svg>
<div class="about-art" role="img" aria-label="Illustration of a dark solar panel with yellow and orange sun rays radiating behind it">
  <div class="about-panel"></div>
</div>
<div class="panels-photo" role="img" aria-label="Photo of a row of blue ground-mounted solar panels"></div>
<div class="about-copy">
  <h2>About Brivane Solar?</h2>
  <div class="sub">Brivane: a derivative of the Latin word Brivanus (noun): partner, ally</div>
  <p>At Brivane Solar, we believe that solid partnerships are the building blocks behind every success story. By approaching every aspect of our business model with transparency and integrity, we have built a foundation of industry-leading experts and lifelong clients.</p>
</div>
<div class="btn-outline" style="left:659px;top:2450px;width:148px;height:44px">LEARN MORE</div>

<!-- reasons -->
<h2 class="display abs" style="left:86px;top:3050px;font-size:35px;line-height:44px;color:var(--navy);font-weight:800">Reasons to<br>Explore Solar</h2>
<svg class="abs" style="left:350px;top:2835px" width="480" height="480" viewBox="0 0 480 480" aria-hidden="true">
  <circle cx="239" cy="239" r="230" fill="none" stroke="#243b4a" stroke-width="1.4" stroke-dasharray="6 5"/>
  <path d="M460 130 L460 350" stroke="#243b4a" stroke-width="1.2" stroke-dasharray="6 5" fill="none"/>
</svg>
<div class="abs" role="img" aria-label="Photo of a white house with rooftop solar panels and a green lawn" style="left:385px;top:2870px;width:408px;height:408px;border-radius:50%;background:linear-gradient(180deg,#4f8fd0 0%,#a7c9ea 40%,#e9e4d6 58%,#7fa356 78%,#5a8a3a 100%)"></div>
<div class="reason-bub" style="left:690px;top:2867px;background:var(--teal)"><svg width="38" height="38" viewBox="0 0 38 38" fill="none" stroke="#fff" stroke-width="2"><rect x="8" y="4" width="22" height="30" rx="2"/><path d="M13 12h12M13 18h12M13 24h7"/></svg></div>
<div class="reason-bub" style="left:768px;top:2960px;background:var(--yellow)"><svg width="38" height="38" viewBox="0 0 38 38" fill="none" stroke="#fff" stroke-width="2"><path d="M19 6c6 4 7 10 0 16-7-6-6-12 0-16zM4 24c5 0 9 4 15 4s10-4 15-4M8 32h22"/></svg></div>
<div class="reason-bub" style="left:768px;top:3085px;background:var(--peach)"><svg width="38" height="38" viewBox="0 0 38 38" fill="none" stroke="#fff" stroke-width="2"><rect x="5" y="16" width="9" height="18"/><rect x="15" y="8" width="9" height="26"/><rect x="25" y="20" width="8" height="14"/></svg></div>
<div class="reason-bub" style="left:690px;top:3179px;background:var(--orange)"><svg width="38" height="38" viewBox="0 0 38 38" fill="none" stroke="#fff" stroke-width="2.4" stroke-linecap="round"><path d="M19 5v13"/><path d="M11 10a12 12 0 1016 0"/></svg></div>

<div class="reason" style="left:796px;top:2852px"><h4>Reduce / Eliminate Utility Bills</h4><p>At Brivane Solar, we believe that solid partnerships are the building...</p></div>
<div class="reason" style="left:870px;top:2970px"><h4>Protect the Environment</h4><p>At Brivane Solar, we believe that solid partnerships are the building...</p></div>
<div class="reason" style="left:876px;top:3100px"><h4>Increase Property Value</h4><p>At Brivane Solar, we believe that solid partnerships are the building...</p></div>
<div class="reason" style="left:796px;top:3221px"><h4>Own Your Power</h4><p>At Brivane Solar, we believe that solid partnerships are the building...</p></div>

<!-- team -->
<h2 class="sec-title" style="top:3396px;font-size:34px">Meet The Team</h2>
<p class="abs" style="left:0;top:3450px;width:1200px;text-align:center;font-size:13px;line-height:22px;color:var(--muted)">The team at Brivane Solar is here to be your ally in the solar industry. We believe in<br>collaborating on best practices while allowing you to drive the decisions.</p>
<div class="btn-outline" style="left:526px;top:3513px;width:148px;height:42px">LEARN MORE</div>
<div class="team-photo" role="img" aria-label="Group photo of the team in matching blue polo shirts standing outdoors"></div>

<!-- footer -->
<svg class="footer-shape" viewBox="0 3960 1200 624" aria-hidden="true">
  <polygon points="0,4238 872,3987 1200,4215 1200,4240 872,4012 0,4262" fill="#2a9d8a"/>
  <polygon points="0,4262 872,4012 1200,4240 1200,4584 0,4584" fill="#243b4a"/>
</svg>

<div class="brand" style="left:105px;top:4303px;color:var(--white);font-size:23px"><span class="brand-dot" style="width:18px;height:18px"></span>Brivane Solar</div>
<p class="abs" style="left:80px;top:4355px;width:260px;text-align:center;color:var(--white);font-size:11.5px;line-height:19px">Brivane: a derivative of the Latin word Brivanus (noun); partner, ally</p>
<div class="abs" style="left:126px;top:4406px;display:flex;gap:7px"><span class="soc"></span><span class="soc"></span><span class="soc"></span><span class="soc"></span></div>

<div class="foot-h" style="left:377px">Contact Info</div>
<div class="contact-item" style="top:4275px"><svg width="12" height="10" viewBox="0 0 12 10"><rect width="12" height="10" rx="1" fill="#e8674a"/><path d="M0 1l6 4 6-4" stroke="#243b4a" fill="none"/></svg><div><b>Email:</b>hello@brivane-example.com</div></div>
<div class="contact-item" style="top:4335px"><svg width="12" height="12" viewBox="0 0 24 24"><path d="M6.6 10.8a15.1 15.1 0 006.6 6.6l2.2-2.2c.3-.3.7-.4 1-.2 1.1.4 2.3.6 3.6.6.6 0 1 .4 1 1V20c0 .6-.4 1-1 1A17 17 0 013 4c0-.6.4-1 1-1h3.5c.6 0 1 .4 1 1 0 1.3.2 2.5.6 3.6.1.3 0 .7-.2 1z" fill="#e8674a"/></svg><div><b>Phone:</b>555.BRIVANE</div></div>
<div class="contact-item" style="top:4395px"><svg width="12" height="14" viewBox="0 0 12 14"><path d="M6 0a5 5 0 015 5c0 4-5 9-5 9S1 9 1 5a5 5 0 015-5z" fill="#e8674a"/><circle cx="6" cy="5" r="2" fill="#243b4a"/></svg><div><b>Location:</b>48 Lakeview Avenue, Suite 210<br>Marlow Springs, Ohio 43990</div></div>

<div class="foot-h" style="left:616px">Recent Posts</div>
<div class="post" style="top:4272px"><div class="thumb" role="img" aria-label="Blog thumbnail photo"></div><div><b>Some blog heading</b><span>25-05-2022</span></div></div>
<div class="post" style="top:4340px"><div class="thumb" role="img" aria-label="Blog thumbnail photo" style="background:linear-gradient(135deg,#3d5c2a,#e3b64a)"></div><div><b>Some blog heading</b><span>25-05-2022</span></div></div>
<div class="post" style="top:4408px;border-bottom:none"><div class="thumb" role="img" aria-label="Blog thumbnail photo" style="background:linear-gradient(135deg,#9db8d4,#7a6a52)"></div><div><b>Some blog heading</b><span>25-05-2022</span></div></div>

<div class="foot-h" style="left:869px">Recent Works</div>
<div class="work" role="img" aria-label="Project photo" style="left:869px;top:4272px"></div>
<div class="work" role="img" aria-label="Project photo" style="left:951px;top:4272px"></div>
<div class="work" role="img" aria-label="Project photo" style="left:1033px;top:4272px"></div>
<div class="work" role="img" aria-label="Project photo" style="left:869px;top:4354px"></div>
<div class="work" role="img" aria-label="Project photo" style="left:951px;top:4354px"></div>
<div class="work" role="img" aria-label="Project photo" style="left:1033px;top:4354px"></div>

<div class="copyright">© 2022 Brivane Solar. All Rights Reserved</div>
<div class="chat"><svg width="22" height="20" viewBox="0 0 22 20"><path d="M11 1C5.5 1 1 4.6 1 9c0 2.2 1.1 4.2 3 5.6L3 19l5-2.4c1 .3 2 .4 3 .4 5.5 0 10-3.6 10-8s-4.5-8-10-8z" fill="#fff"/></svg></div>

</body>
</html>
```